mental health business card

Double sided business card with logo on front and practitioners details on back.
The front of card should be while and back either blue or grey to match logo.

Space on back for appointment date and time to be written.

Please note that details are not available yet for address etc as currently moving 4500km across Australia. Just use generic or old info from attached letterhead.
Updates

Dear Designers,

Please note business card is also appointment card must have area where  date and time of clients next appointment can be written in.

Target Market(s)

This is card for patients and colleagues

Industry/Entity Type

Mental Health

Requirements
Must have
• Name
Director / Clinical Psychologist
email
web
phone
phone

Nice to have
• embossing on front of card

```html
<!DOCTYPE html>
<html lang="en">
<head>
<meta charset="utf-8">
<title>Clearwater Mental Health – Business &amp; Appointment Card</title>
<link href="https://fonts.googleapis.com/css2?family=Questrial&display=swap" rel="stylesheet">
<style>
  :root {
    --backdrop: #2b2b2d;
    --card-white: #ffffff;
    --card-mist: #e4e6e9;
    --brand-navy: #173a66;
    --brand-blue: #1b7fab;
    --brand-deep: #112552;
    --brand-grey: #7a7c80;
    --grey-light: #b9bbbf;
    --text-grey: #7d7f84;
    --rule: #cfd2d6;
    --white: #ffffff;
  }
  * { margin: 0; padding: 0; box-sizing: border-box; }
  html, body { width: 1200px; height: 1000px; overflow: hidden; }
  body {
    background: var(--backdrop);
    font-family: "Questrial", "Century Gothic", sans-serif;
    position: relative;
  }
  .card {
    position: absolute;
    left: 250px;
    width: 700px;
    height: 420px;
    border-radius: 22px;
    overflow: hidden;
  }
  .card-shapes { position: absolute; inset: 0; width: 100%; height: 100%; }

  /* Front: appointment side */
  .card--front { top: 70px; background: linear-gradient(135deg, var(--card-white) 30%, var(--card-mist)); }
  .office { position: absolute; left: 140px; top: 46px; font-size: 16px; line-height: 1.3; color: var(--text-grey); }
  .office-label { color: var(--brand-blue); font-style: italic; }
  .appointment { position: absolute; left: 140px; top: 100px; width: 260px; }
  .appointment-title { font-size: 17px; font-weight: 700; color: var(--brand-navy); letter-spacing: 0.5px; padding-bottom: 4px; border-bottom: 1px solid var(--rule); }
  .appointment-field { font-size: 15px; color: var(--text-grey); height: 32px; line-height: 32px; border-bottom: 1px solid var(--rule); }
  .front-web { position: absolute; right: 26px; top: 70px; font-size: 14px; color: var(--text-grey); }
  .brand { position: absolute; left: 46px; top: 268px; display: flex; align-items: center; gap: 18px; }
  .brand-square { width: 74px; height: 74px; border-radius: 8px; background: var(--brand-navy); }
  .brand-name { font-size: 40px; color: var(--brand-navy); letter-spacing: 1px; line-height: 1.05; }

  /* Back: practitioner side */
  .card--back { top: 530px; background: linear-gradient(150deg, var(--brand-blue) 0%, var(--brand-navy) 45%, var(--brand-deep) 100%); }
  .back-web { position: absolute; right: 40px; top: 28px; font-size: 16px; color: var(--white); }
  .back-brand { position: absolute; left: 50px; top: 70px; font-size: 38px; color: var(--white); line-height: 1.05; letter-spacing: 1px; }
  .practitioner { position: absolute; left: 50px; bottom: 44px; color: var(--grey-light); font-size: 18px; line-height: 1.45; }
  .practitioner-name { font-size: 22px; font-weight: 700; color: var(--white); letter-spacing: 0.5px; }
  .practitioner-role { margin-bottom: 10px; }
</style>
</head>
<body>

<section class="card card--front" aria-label="Card front with appointment details">
  <svg class="card-shapes" viewBox="0 0 700 420" preserveAspectRatio="none" aria-hidden="true">
    <defs>
      <linearGradient id="bandBlue" x1="0" y1="0" x2="0" y2="1">
        <stop offset="0" stop-color="#2a9bc6"/>
        <stop offset="1" stop-color="#184c86"/>
      </linearGradient>
      <linearGradient id="greyPanel" x1="0" y1="0" x2="1" y2="1">
        <stop offset="0" stop-color="#a9abaf"/>
        <stop offset="1" stop-color="#d3d5d8"/>
      </linearGradient>
    </defs>
    <path d="M440 0 C470 170 525 320 570 420 L700 420 L700 0 Z" fill="url(#bandBlue)"/>
    <path d="M480 0 C500 150 560 300 625 420 L700 420 L700 0 Z" fill="url(#greyPanel)"/>
  </svg>
  <p class="office"><span class="office-label">Head Office:</span> Unit 12, 48 Harbour Lane,<br>Westfield</p>
  <div class="appointment">
    <p class="appointment-title">APPOINTMENT DETAILS</p>
    <p class="appointment-field">Date:</p>
    <p class="appointment-field">Time:</p>
  </div>
  <p class="front-web">www.clearwatermh.com</p>
  <div class="brand">
    <span class="brand-square"></span>
    <p class="brand-name">CLEARWATER<br>MENTAL HEALTH</p>
  </div>
</section>

<section class="card card--back" aria-label="Card back with practitioner details">
  <svg class="card-shapes" viewBox="0 0 700 420" preserveAspectRatio="none" aria-hidden="true">
    <defs>
      <linearGradient id="backGrey" x1="0" y1="0" x2="1" y2="1">
        <stop offset="0" stop-color="#6f7175"/>
        <stop offset="1" stop-color="#8e9094"/>
      </linearGradient>
    </defs>
    <path d="M240 0 C400 80 560 170 700 320 L700 0 Z" fill="#f1f2f4"/>
    <path d="M300 0 C450 60 590 130 700 215 L700 0 Z" fill="url(#backGrey)"/>
  </svg>
  <p class="back-web">www.clearwatermh.com</p>
  <p class="back-brand">CLEARWATER<br>MENTAL HEALTH</p>
  <div class="practitioner">
    <p class="practitioner-name">MARA ELLISON</p>
    <p class="practitioner-role">Director / Clinical Psychologist</p>
    <p class="practitioner-email">mara.ellison@clearwatermh.com</p>
    <p class="practitioner-phone">150 4621 3098</p>
  </div>
</section>

</body>
</html>
```